An hotel welcome folder kit
luxury suites in NYC
An hotel  welcome folder kit -
Creative Brief
We are looking for to set up a beautiful welcome folder for our suites guests. This folder will be placed in the room on the bed. Within this folder they will find the whole info they need in order to get around the building they are staying in,about our services, the location. amenities, attractions etc. here is some info about what our business about: Morvane Lodgings offers various luxury vacation suites in beautiful luxury residential buildings around Manhattan and are rented out to tourists on a short term basis a la a hotel. The suites and buildings come fully equipped with all the necessary amenities and more: - wireless internet & high definition television with digital cable in unit - On site laundry room - Fantastic fully equipped gym - Residential lounge area with billiards table - Amazing roof deck with breathtaking views of the city.
our suites guests.
The welcome kit is a folder that has a one pocket on the right hand side of the folder inside. in this pocket we will place the pages with the info the guests need to know. on the left hand side inside the folder we will pitch our hotel concept (1-2 short sentences). on the cover of the folder we would like to see our logo and the name of the hotel the logo file is attached. what do we need from you: 1.a design of the folder based on our logo (colors ans font) : cover , left hand side inside the folder, on the back of the folder our contact info 2. a design of a template for the pages that we will place inside the folder (each page has its own topic for example: one page is about our services, the second page is info about attractions in the city..etc) important: the design should present out consept of luxury , high end style, Cutting-Edge Unique/Creative,Clean/Simple, Sophisticated. info about the logo: Brown #CFBA76 R:207 G:186 B:118 Font:Rage Italic Font2: Arial tagline: Arial dark Gray: #333333 R:51 G:51 B:51 Thanks a lot!!!

```html
<!DOCTYPE html>
<html lang="en">
<head>
<meta charset="utf-8">
<title>Morvane Lodgings – Welcome Folder, Inside Spread</title>
<link href="https://fonts.googleapis.com/css2?family=Cinzel:wght@400;600&family=Great+Vibes&family=Arimo:ital,wght@0,400;0,700;1,400;1,700&display=swap" rel="stylesheet">
<style>
  :root{
    --gold:#cfba76;
    --gold-deep:#a8904e;
    --gold-pale:#e9dfc0;
    --ink:#333333;
    --black:#0b0b0b;
    --paper:#ffffff;
    --sepia-light:#e4dac4;
    --sepia-mid:#b49f78;
    --sepia-dark:#4a3a26;
  }
  *{margin:0;padding:0;box-sizing:border-box}
  html,body{width:1200px;height:833px;overflow:hidden;background:var(--paper)}
  body{position:relative;font-family:"Arimo",Arial,sans-serif;color:var(--ink)}

  .panel-label{position:absolute;top:2px;font-size:15px;color:var(--ink)}
  .panel-label.inside-1{left:10px}
  .panel-label.inside-2{left:612px}

  .title-band{
    position:absolute;left:0;top:24px;width:1200px;height:72px;
    background:linear-gradient(90deg,#d9ccaa 0%,#f1ead6 40%,#efe6cf 60%,#cdb98a 100%);
  }
  .title-band h1{
    font-family:"Cinzel",serif;font-weight:400;font-size:44px;letter-spacing:3px;
    color:var(--gold-deep);text-align:center;line-height:72px;
  }

  /* Inside 1 */
  .inside-left{
    position:absolute;left:0;top:96px;width:605px;height:684px;overflow:hidden;
  }
  .inside-left .room-photo{
    position:absolute;inset:0;
    background:
      radial-gradient(ellipse 140px 160px at 470px 130px,#fbf2d8 0%,rgba(230,210,160,.6) 45%,rgba(0,0,0,0) 100%),
      linear-gradient(90deg,var(--sepia-light) 0%,#dccfb2 42%,var(--sepia-mid) 62%,#7d6647 80%,var(--sepia-dark) 100%);
  }
  .copy{position:absolute;left:24px;top:12px;width:280px}
  .script-heading{
    font-family:"Great Vibes",cursive;font-size:44px;color:var(--gold-deep);line-height:1;
    font-weight:400;margin-bottom:4px;
  }
  .lead{
    font-style:italic;font-weight:700;font-size:13.5px;line-height:17px;color:var(--gold-deep);
    margin-bottom:10px;
  }
  .body-text{font-size:9.6px;line-height:12.4px;color:var(--ink);margin-bottom:8px}
  .facilities{margin-top:20px}
  .amenities-intro{font-weight:700;font-size:10px;line-height:13px;margin-bottom:2px}
  .amenities{list-style:none;font-size:9.4px;line-height:12.2px}
  .amenities li::before{content:"• "}

  /* Inside 2 */
  .inside-right{
    position:absolute;left:605px;top:96px;width:595px;height:684px;background:var(--black);overflow:hidden;
  }
  .inside-right .frame{position:absolute;inset:0}
  .brand{position:absolute;left:32px;top:78px;color:var(--paper)}
  .brand-name{display:flex;align-items:center;gap:8px;font-family:"Arimo",Arial,sans-serif;font-weight:700;font-size:24px;color:var(--gold)}
  .brand-dot{width:14px;height:14px;border-radius:50%;background:var(--gold)}
  .brand-tagline{font-size:11px;margin:4px 0 0 22px;color:var(--paper)}
  .slogan{
    position:absolute;right:20px;top:80px;width:220px;text-align:right;
    font-weight:700;font-style:italic;font-size:17px;line-height:22px;color:var(--paper);
  }
  .bridge-photo{
    position:absolute;left:266px;top:136px;width:329px;height:488px;
    background:
      linear-gradient(180deg,#1d3a80 0%,#3e69b8 30%,#8fb0d8 55%,#6d6a62 75%,#3b3229 100%);
    border-left:3px solid var(--gold);
  }
  .feature{position:absolute;left:14px;top:270px;width:240px}
  .feature h2{font-weight:700;font-style:italic;font-size:14.5px;line-height:17px;color:var(--paper);margin-bottom:8px}
  .feature p{font-size:8.4px;line-height:11px;color:#bdbdbd}
</style>
</head>
<body>
  <div class="panel-label inside-1">Inside-1</div>
  <div class="panel-label inside-2">Inside-2</div>

  <header class="title-band"><h1>LUXURY SUITES IN NYC</h1></header>

  <section class="inside-left">
    <div class="room-photo" role="img" aria-label="Sepia photograph of a luxury bedroom with a crystal candelabra lamp on an ornate bedside table"></div>
    <div class="copy">
      <h2 class="script-heading">Suites</h2>
      <p class="lead">If you are dreaming of rest, relaxation and tranquility in a stunning setting with truly personal service, then we can make your Morvane come true.</p>
      <p class="body-text">Morvane Luxury Suites is the place where style, opulence, and perfection meet a world of beauty and tradition. They represent a new concept of luxury with just five luxury suites that have a unique personality, and combine courteous and warm service with authentic tradition. The Suites were designed for the distinctive guest who is able to appreciate a singular kind of comfort, class, space and tranquillity.</p>
      <p class="body-text">Our Luxury Suites, and the staff serving them are unique, and we are dedicated to making our guests feel unique too.</p>
      <p class="body-text">Each Luxury Suite is designed in the traditional Cycladic style, and has its own terrace with a Swimming Pool or Jacuzzi overlooking the Caldera and the Aegean Sea. Our Suites have shaped true to the original style of the island and represent an inimitable sample of traditional Greek architecture. The privileged location of the Suites provide a nearly step-free access.</p>

      <h2 class="script-heading facilities">Facilities</h2>
      <p class="lead">Morvane Lodgings offers various luxury vacation suites in beautiful luxury residential buildings around Manhattan and are rented out to tourists on a short term basis a la a hotel.</p>
      <p class="amenities-intro">The suites and buildings come fully equipped with all the necessary amenities and more:</p>
      <ul class="amenities">
        <li>Wireless internet &amp; high definition television with digital cable in unit</li>
        <li>On site laundry room</li>
        <li>Fantastic fully equipped gym</li>
        <li>Residential lounge area with billiards table</li>
        <li>Amazing roof deck with breathtaking views of the city.</li>
      </ul>
    </div>
  </section>

  <section class="inside-right">
    <div class="bridge-photo" role="img" aria-label="Photograph of the stone towers and cables of a suspension bridge under a blue sky with a flag"></div>
    <svg class="frame" width="595" height="684" viewBox="0 0 595 684" aria-hidden="true">
      <defs>
        <linearGradient id="goldSweep" x1="0" x2="1" y1="0" y2="0">
          <stop offset="0" stop-color="#e9dfc0"/>
          <stop offset=".5" stop-color="#cfba76"/>
          <stop offset="1" stop-color="#a8904e"/>
        </linearGradient>
      </defs>
      <path d="M0 0 H595 V40 C470 20 330 30 170 62 C100 75 40 70 0 60 Z" fill="url(#goldSweep)"/>
      <path d="M0 60 C40 70 100 75 170 62 C330 30 470 20 595 40" fill="none" stroke="#0b0b0b" stroke-width="4"/>
      <path d="M0 475 C150 450 300 470 420 505 C500 528 560 535 595 530 V684 H0 Z" fill="#0b0b0b"/>
      <path d="M0 475 C150 450 300 470 420 505 C500 528 560 535 595 530" fill="none" stroke="url(#goldSweep)" stroke-width="5"/>
    </svg>
    <div class="brand">
      <div class="brand-name"><span class="brand-dot"></span>Morvane Lodgings</div>
      <div class="brand-tagline">luxury suites in NYC</div>
    </div>
    <p class="slogan">A WONDERFULL<br>RESTFUL STAY</p>
    <div class="feature">
      <h2>Lorem ipsum dolor sit amet,<br>Sed varius suscipit neque</h2>
      <p>Lorem ipsum dolor sit amet, consectetur adipiscing elit. Donec enim augue, tempor molestie auctor eu, venenatis eu ante. Sed varius suscipit neque et aliquam. Nam nec dui sed sapien suscipit fringilla. Cras bibendum nisi sit amet erat venenatis tincidunt. Integer a dictum purus. Pellentesque habitant morbi tristique senectus et netus.</p>
    </div>
  </section>
</body>
</html>
```